Hi,

I have just started up a business called VOLMIRA in Melbourne. We run fun street art tours around Melbourne's CBD.

I need to create a design for the back side of my business cards. I have designed the front side (simply with my logo) however, I am having trouble designing the reverse side in a professional manner. I have attached pictures of what I have done.

The picture attached titled "VOLMIRA Business Cards Back" has all the information that I require on the back side of my business cards; although displayed in an amateur and simple way. As displayed in the picture, I need: the VOLMIRA logo, the website URL, the booking details (phone - 0468 152 837 & email - bookings@volmira-example.com.au) and the service description ($20, One Hour, Tours Daily, Meet at Halberton St Station). I would also like to use the font in the picture supplied which is "source-sans-pro".

The VOLMIRA tours are for tourists and are relaxed, entertaining and fun! I would like the design to reflect this.

Target Market(s)

Backpackers & University Students

Industry/Entity Type

Business

Requirements
Must have
• The VOLMIRA logo, the website URL, the booking details (phone - 0468 152 837 & email - bookings@volmira-example.com.au) and the service description ($20, One Hour, Tours Daily, Meet at Halberton St Station).

```html
<!DOCTYPE html>
<html lang="en">
<head>
<meta charset="utf-8">
<title>VOLMIRA Business Cards</title>
<link rel="stylesheet" href="https://fonts.googleapis.com/css2?family=Source+Sans+3:wght@400;600;700&display=swap">
<style>
  :root {
    --backdrop: #5a626a;
    --card: #e4e2e0;
    --ink: #111111;
    --brand-red: #e0443c;
    --accent-blue: #1e88d8;
    --icon-blue: #39a6ee;
    --splash-orange: #f5921e;
    --splash-lime: #d6e021;
    --white: #ffffff;
  }
  * { margin: 0; padding: 0; box-sizing: border-box; }
  html, body { width: 1200px; height: 900px; overflow: hidden; }
  body {
    background: var(--backdrop);
    font-family: "Source Sans 3", "Source Sans Pro", Arial, sans-serif;
    color: var(--ink);
    position: relative;
  }
  .card {
    position: absolute;
    background: var(--card);
    box-shadow: 0 6px 14px rgba(0,0,0,0.35);
    overflow: hidden;
  }
  .card-front { left: 62px; top: 30px; width: 625px; height: 365px; }
  .card-back { left: 452px; top: 425px; width: 695px; height: 420px; }

  .brand-name {
    position: absolute;
    font-weight: 700;
    color: var(--brand-red);
    letter-spacing: 2px;
    line-height: 1;
  }
  .card-front .brand-name { left: 0; right: 0; top: 110px; text-align: center; font-size: 62px; }
  .tagline {
    position: absolute; left: 0; right: 0; top: 210px;
    text-align: center; font-weight: 600; font-size: 40px; line-height: 1.3;
  }

  .card-back .brand-name { left: 50px; top: 90px; font-size: 46px; }
  .call-to-book {
    position: absolute; left: 53px; top: 178px;
    color: var(--accent-blue); font-weight: 600; font-size: 21px; letter-spacing: -0.2px;
  }
  .contact-list { position: absolute; left: 48px; top: 222px; list-style: none; }
  .contact-list li {
    display: flex; align-items: center; gap: 14px;
    font-size: 21px; height: 35px;
  }
  .contact-icon { width: 24px; height: 24px; flex: none; }

  .splash { position: absolute; }
  .splash-orange { left: 330px; top: 0; width: 365px; height: 250px; }
  .splash-lime { left: 395px; top: 215px; width: 300px; height: 205px; }

  .offer {
    position: absolute; left: 428px; top: 40px;
    font-weight: 600; line-height: 1;
  }
  .offer-price { font-size: 58px; font-weight: 700; }
  .offer-daily { font-size: 44px; color: var(--white); margin-top: 6px; }
  .offer-length { font-size: 44px; margin-top: 4px; }
  .meeting-point {
    position: absolute; left: 478px; top: 252px;
    font-size: 32px; font-weight: 600; line-height: 1.2;
  }
</style>
</head>
<body>
  <section class="card card-front">
    <div class="brand-name">VOLMIRA</div>
    <p class="tagline">Melbourne Street Art<br>Walking Tours</p>
  </section>

  <section class="card card-back">
    <svg class="splash splash-orange" viewBox="0 0 365 250" role="img" aria-label="Orange paint splash background">
      <path d="M40 0 H365 V235 L300 245 L210 230 L120 240 L60 215 L80 170 L20 150 L50 110 L0 70 L45 40 Z" fill="var(--splash-orange)"/>
    </svg>
    <svg class="splash splash-lime" viewBox="0 0 300 205" role="img" aria-label="Lime paint splash background">
      <path d="M60 10 L160 0 L240 15 L300 5 V205 H40 L70 160 L20 120 L60 80 L30 40 Z" fill="var(--splash-lime)"/>
    </svg>

    <div class="brand-name">VOLMIRA</div>
    <p class="call-to-book">CALL TOMAS TO BOOK NOW!</p>
    <ul class="contact-list">
      <li>
        <svg class="contact-icon" viewBox="0 0 24 24" aria-hidden="true">
          <circle cx="12" cy="12" r="12" fill="var(--icon-blue)"/>
          <path d="M8 6.5 L10 6.5 L11 9.5 L9.6 10.6 Q11 13.4 13.4 14.4 L14.5 13 L17.5 14 L17.5 16 Q17 17.6 15 17.5 Q7.5 16.5 6.5 8.5 Q6.6 6.8 8 6.5 Z" fill="var(--ink)"/>
        </svg>
        <span>0468 152 837</span>
      </li>
      <li>
        <svg class="contact-icon" viewBox="0 0 24 24" aria-hidden="true">
          <circle cx="12" cy="12" r="12" fill="var(--icon-blue)"/>
          <text x="12" y="17" text-anchor="middle" font-size="15" font-weight="700" fill="var(--ink)" font-family="Source Sans 3, sans-serif">@</text>
        </svg>
        <span>bookings@volmira-example.com.au</span>
      </li>
      <li>
        <svg class="contact-icon" viewBox="0 0 24 24" aria-hidden="true">
          <circle cx="12" cy="12" r="12" fill="var(--icon-blue)"/>
          <g fill="none" stroke="var(--ink)" stroke-width="1.4">
            <circle cx="12" cy="12" r="6"/>
            <ellipse cx="12" cy="12" rx="2.6" ry="6"/>
            <line x1="6" y1="12" x2="18" y2="12"/>
          </g>
        </svg>
        <span>www.volmira-example.com.au</span>
      </li>
    </ul>

    <div class="offer">
      <div class="offer-price">$20</div>
      <div class="offer-daily">Tours Daily</div>
      <div class="offer-length">One Hour</div>
    </div>
    <p class="meeting-point">Meet at<br>Halberton<br>St Station</p>
  </section>
</body>
</html>
```